Business Card For Kelmora Financial Consulting

Hi, I would like a business card designed. Bold, modern.
Please use the same design as the logo. I have also attached the website design to see the overall theme.
Wordmark Font
Color: Hex: #01AEF7

```html
<!DOCTYPE html>
<html lang="en">
<head>
<meta charset="utf-8">
<title>Kelmora Financial Consulting — Business Card</title>
<link href="https://fonts.googleapis.com/css2?family=Raleway:wght@400;500;800&display=swap" rel="stylesheet">
<style>
  :root {
    --stage: #170040;
    --paper: #f4f4f4;
    --ink: #18252e;
    --accent: #01aef7;
    --white: #ffffff;
  }
  * { margin: 0; padding: 0; box-sizing: border-box; }
  html, body { width: 1200px; height: 1200px; overflow: hidden; background: var(--stage); }
  .canvas { position: relative; width: 1200px; height: 1200px; font-family: "Raleway", sans-serif; }

  .card-front {
    position: absolute; left: 131px; top: 78px; width: 950px; height: 522px;
    background: var(--paper); border-radius: 16px; overflow: hidden;
  }
  .front-band { position: absolute; left: 0; bottom: 0; width: 100%; height: 20px; }
  .brand-front {
    position: absolute; left: 62px; top: 239px;
    display: flex; align-items: center; gap: 14px;
  }
  .brand-square { width: 44px; height: 44px; background: var(--accent); flex: none; }
  .brand-name-front {
    font-weight: 800; font-size: 24px; letter-spacing: 0.5px;
    color: var(--ink); text-transform: uppercase; white-space: nowrap;
  }
  .divider {
    position: absolute; left: 472px; top: 88px; width: 4px; height: 374px; background: var(--ink);
  }
  .person-name {
    position: absolute; left: 527px; top: 105px;
    font-weight: 500; font-size: 38px; color: var(--ink);
  }
  .contact-list { position: absolute; left: 510px; top: 188px; list-style: none; }
  .contact-item {
    display: flex; align-items: center; height: 72px;
    font-weight: 500; font-size: 17px; color: var(--ink);
  }
  .contact-icon { width: 34px; height: 34px; margin-right: 26px; flex: none; }

  .card-back {
    position: absolute; left: 119px; top: 640px; width: 949px; height: 521px;
    background: var(--ink); border-radius: 16px;
    display: flex; align-items: center; justify-content: center;
  }
  .brand-name-back {
    font-weight: 800; font-size: 38px; letter-spacing: 2px;
    color: var(--white); text-transform: uppercase; white-space: nowrap;
  }
</style>
</head>
<body>
<main class="canvas">
  <section class="card-front">
    <div class="brand-front">
      <span class="brand-square"></span>
      <span class="brand-name-front">Kelmora Consulting</span>
    </div>
    <span class="divider"></span>
    <h1 class="person-name">John Doe</h1>
    <ul class="contact-list">
      <li class="contact-item">
        <svg class="contact-icon" viewBox="0 0 24 24" aria-hidden="true"><path fill="#18252e" d="M6.6 10.8a15.1 15.1 0 0 0 6.6 6.6l2.2-2.2a1 1 0 0 1 1-.25 11.4 11.4 0 0 0 3.6.57 1 1 0 0 1 1 1V20a1 1 0 0 1-1 1A17 17 0 0 1 3 4a1 1 0 0 1 1-1h3.5a1 1 0 0 1 1 1c0 1.25.2 2.45.57 3.57a1 1 0 0 1-.25 1z"/></svg>
        <span>000 . 011 . 111 . 001</span>
      </li>
      <li class="contact-item">
        <svg class="contact-icon" viewBox="0 0 24 24" aria-hidden="true"><path fill="#18252e" d="M2 5h20v14H2z"/><path fill="none" stroke="#f4f4f4" stroke-width="1.6" d="M2.5 5.8 12 13l9.5-7.2"/></svg>
        <span>www.kelmoraconsulting@gmail.com</span>
      </li>
      <li class="contact-item">
        <svg class="contact-icon" viewBox="0 0 24 24" aria-hidden="true"><g fill="none" stroke="#18252e" stroke-width="1.5"><circle cx="12" cy="12" r="10"/><ellipse cx="12" cy="12" rx="4.5" ry="10"/><path d="M2 12h20M3.5 7h17M3.5 17h17M12 2v20"/></g></svg>
        <span>www.kelmoraconsulting.com</span>
      </li>
    </ul>
    <svg class="front-band" viewBox="0 0 950 20" preserveAspectRatio="none" aria-hidden="true">
      <rect width="950" height="20" fill="#18252e"/>
      <polygon points="640,0 950,0 950,20 620,20" fill="#01aef7"/>
    </svg>
  </section>

  <section class="card-back">
    <span class="brand-name-back">Kelmora Consulting</span>
  </section>
</main>
</body>
</html>
```